Boutique custom software development company needs new business card

Our nearly 20 year old custom software development company would like to better include the fact that we are now providing Bitcoin services. These new services are B2B include education (how to acquire and securely hold Bitcoin) and integrating Bitcoin payments into existing ecommerce sites or other existing systems. Please keep the card clean and simple. Attached is our current design and some other files. vexalon.example

Target Market(s)

businesses owners interested in long term relationship

Industry/Entity Type

Custom software development and Bitcoin

Contact Information for Business Card

Marcus Ellwood, marcus@vexalon.example, vexalon.example, (888) 555-VEXAL

Font styles to use
Other font styles liked:
• monospace

Requirements
Must have
• double-sided
Nice to have
• clean and simple
Should not have
• physical address

```html
<!DOCTYPE html>
<html lang="en">
<head>
<meta charset="utf-8">
<title>Vexalon Business Card</title>
<link rel="stylesheet" href="https://fonts.googleapis.com/css2?family=Montserrat:wght@400;500;700;800&family=Lato:wght@400&family=JetBrains+Mono:wght@400;500&display=swap">
<style>
  :root {
    --backdrop: #9a9a9a;
    --paper: #f7f7f6;
    --brand-blue: #3b72b9;
    --brand-orange: #ef7d22;
    --ink-grey: #555555;
    --white: #ffffff;
  }
  * { box-sizing: border-box; margin: 0; padding: 0; }
  html, body { width: 1200px; height: 952px; overflow: hidden; }
  body {
    background: var(--backdrop);
    font-family: "Montserrat", sans-serif;
    position: relative;
  }
  .card {
    position: absolute;
    left: 250px;
    width: 700px;
    height: 400px;
    border-radius: 4px;
    box-shadow: 0 10px 30px rgba(0,0,0,0.25);
    border-bottom: 3px solid var(--brand-orange);
    overflow: hidden;
  }
  .card--front { top: 56px; background: var(--paper); }
  .card--back { top: 496px; background: var(--brand-blue); }

  .wordmark { position: absolute; }
  .wordmark__name {
    font-family: "Montserrat", sans-serif;
    font-weight: 800;
    font-size: 60px;
    letter-spacing: 1px;
    line-height: 1;
  }
  .wordmark__tagline {
    font-family: "Lato", sans-serif;
    font-size: 20px;
    margin-top: 6px;
    letter-spacing: 0.2px;
  }
  .card--front .wordmark { right: 56px; top: 72px; text-align: right; }
  .card--front .wordmark__name,
  .card--front .wordmark__tagline { color: var(--brand-blue); }

  .card--back .wordmark { left: 70px; top: 120px; }
  .card--back .wordmark__name,
  .card--back .wordmark__tagline { color: var(--white); }

  .services {
    list-style: none;
    margin-top: 26px;
    font-family: "JetBrains Mono", monospace;
    font-size: 14px;
    font-weight: 500;
    color: var(--white);
    line-height: 24px;
    letter-spacing: 0.3px;
  }
  .services__item::before {
    content: "";
    display: inline-block;
    width: 8px; height: 8px;
    margin-right: 10px;
    background: var(--brand-orange);
    vertical-align: 1px;
  }

  .identity { position: absolute; left: 60px; top: 192px; }
  .identity__name {
    font-weight: 700;
    font-size: 24px;
    letter-spacing: 2px;
    text-transform: uppercase;
  }
  .identity__first { color: var(--brand-orange); }
  .identity__last { color: var(--brand-blue); }
  .identity__role {
    font-weight: 400;
    font-size: 15px;
    color: var(--ink-grey);
    margin-top: 2px;
    letter-spacing: 0.5px;
  }
  .divider {
    position: absolute;
    left: 60px; right: 60px; top: 256px;
    height: 1px;
    background: var(--brand-orange);
  }
  .contact {
    position: absolute;
    left: 60px; top: 270px;
    list-style: none;
  }
  .contact__item {
    display: flex;
    align-items: center;
    gap: 9px;
    font-size: 14px;
    font-weight: 500;
    color: var(--ink-grey);
    letter-spacing: 0.6px;
    line-height: 25px;
  }
  .contact__icon { width: 13px; height: 13px; fill: var(--brand-blue); flex: none; }
  .front-services {
    position: absolute;
    right: 60px; bottom: 40px;
    font-family: "JetBrains Mono", monospace;
    font-size: 12px;
    color: var(--brand-orange);
    letter-spacing: 0.3px;
    text-align: right;
  }
</style>
</head>
<body>

  <section class="card card--front" aria-label="Card front">
    <div class="wordmark">
      <div class="wordmark__name">VEXALON</div>
      <div class="wordmark__tagline">developer of custom applications</div>
    </div>

    <div class="identity">
      <div class="identity__name"><span class="identity__first">Marcus</span> <span class="identity__last">Ellwood</span></div>
      <div class="identity__role">Owner</div>
    </div>

    <div class="divider"></div>

    <ul class="contact">
      <li class="contact__item">
        <svg class="contact__icon" viewBox="0 0 24 24" aria-hidden="true"><path d="M6.6 10.8a15.1 15.1 0 0 0 6.6 6.6l2.2-2.2c.3-.3.7-.4 1-.2 1.1.4 2.3.6 3.6.6.6 0 1 .4 1 1V20c0 .6-.4 1-1 1C10.6 21 3 13.4 3 4c0-.6.4-1 1-1h3.5c.6 0 1 .4 1 1 0 1.3.2 2.5.6 3.6.1.3 0 .7-.2 1z"/></svg>
        (888) 555-VEXAL
      </li>
      <li class="contact__item">
        <svg class="contact__icon" viewBox="0 0 24 24" aria-hidden="true"><path d="M2 5h20v14H2z M2 5l10 8 10-8" fill="none" stroke="#3b72b9" stroke-width="2.4"/></svg>
        marcus@vexalon.example
      </li>
      <li class="contact__item">
        <svg class="contact__icon" viewBox="0 0 24 24" aria-hidden="true"><circle cx="12" cy="12" r="10" fill="none" stroke="#3b72b9" stroke-width="2.4"/><path d="M2 12h20M12 2c3 3 3 17 0 20M12 2c-3 3-3 17 0 20" fill="none" stroke="#3b72b9" stroke-width="1.8"/></svg>
        www.vexalon.example
      </li>
    </ul>

    <p class="front-services">custom software · bitcoin services</p>
  </section>

  <section class="card card--back" aria-label="Card back">
    <div class="wordmark">
      <div class="wordmark__name">VEXALON</div>
      <div class="wordmark__tagline">developer of custom applications</div>
      <ul class="services">
        <li class="services__item">Bitcoin education &amp; secure custody</li>
        <li class="services__item">Bitcoin payment integration</li>
      </ul>
    </div>
  </section>

</body>
</html>
```